Business Cards for Retail/Sourcing Business.

We need a business cards for our company where it looks like:
TK
LM

VERTICAL, where the TK is over the LM. Then Under the TKLM would be name, address and website address. We want the P to be in the style of our original logo, which I uploaded.

Also, can we get a couple of designs with fun colors - especially for the letter head.

Target Market(s)

Old clients. Many of our clients or people we do business with are 40-50 plus. We are not an industry with many young people.

Industry/Entity Type

Business

Contact Information for Business Card

Front side is just says TKLM with name, title, address, and website below.

Font styles to use
Serif
Sans Serif
Decorative
Script

Requirements
Must have
• THE TKLM design with the P in the design of the logo
Nice to have
• Fun colors, new takes on the TKLM and any other additions that would be cool and make it pop

```html
<!DOCTYPE html>
<html lang="en">
<head>
<meta charset="utf-8">
<title>TKLM Business Card</title>
<link rel="stylesheet" href="https://fonts.googleapis.com/css2?family=Open+Sans:wght@400;700&display=swap">
<style>
  :root {
    --backdrop: #bbbbbb;
    --paper: #ffffff;
    --ink: #000000;
    --rim: #5a5a5a;
    --reverse-text: #ffffff;
  }
  html, body {
    margin: 0;
    padding: 0;
    width: 1200px;
    height: 1000px;
    overflow: hidden;
    background: var(--backdrop);
    font-family: "Open Sans", Arial, sans-serif;
  }
  .business-card {
    position: absolute;
    left: 350px;
    top: 70px;
    width: 500px;
    height: 860px;
    background: var(--paper);
    overflow: hidden;
    box-shadow: 0 6px 18px rgba(0,0,0,0.25);
  }
  .card-shapes {
    position: absolute;
    inset: 0;
  }
  .card-shapes .rim { fill: var(--rim); }
  .card-shapes .panel { fill: var(--ink); }
  .wordmark {
    position: absolute;
    left: 70px;
    top: 110px;
    color: var(--ink);
    font-weight: 700;
    font-size: 112px;
    line-height: 0.92;
    letter-spacing: 2px;
  }
  .wordmark .row-two { display: block; padding-left: 58px; }
  .holder {
    position: absolute;
    left: 120px;
    top: 560px;
    color: var(--reverse-text);
  }
  .holder-name {
    margin: 0;
    font-size: 31px;
    font-weight: 700;
    letter-spacing: 1px;
    text-transform: uppercase;
  }
  .holder-title {
    margin: 4px 0 0 120px;
    font-size: 17px;
    font-weight: 400;
  }
  .contact {
    position: absolute;
    left: 120px;
    top: 718px;
    color: var(--reverse-text);
    font-size: 21px;
    line-height: 1.3;
    list-style: none;
    margin: 0;
    padding: 0;
  }
  .contact li { display: flex; align-items: center; }
  .contact .indent { padding-left: 32px; }
  .contact .globe { width: 20px; height: 20px; margin-right: 12px; }
</style>
</head>
<body>
  <article class="business-card">
    <svg class="card-shapes" width="500" height="860" viewBox="0 0 500 860" aria-hidden="true">
      <path class="rim" d="M0 470 C 40 340, 250 318, 500 318 L500 860 L0 860 Z"/>
      <path class="panel" d="M0 490 C 45 360, 255 336, 500 336 L500 860 L0 860 Z"/>
    </svg>

    <div class="wordmark" aria-label="TKLM">
      <span class="row-one">TK</span>
      <span class="row-two">LM</span>
    </div>

    <header class="holder">
      <h1 class="holder-name">Marla Winslow</h1>
      <p class="holder-title">Home Sourcing</p>
    </header>

    <ul class="contact">
      <li>
        <svg class="globe" viewBox="0 0 20 20" aria-hidden="true">
          <circle cx="10" cy="10" r="9" fill="#fff"/>
          <g fill="none" stroke="#000" stroke-width="1.2">
            <ellipse cx="10" cy="10" rx="4" ry="8"/>
            <line x1="2" y1="10" x2="18" y2="10"/>
            <line x1="10" y1="2" x2="10" y2="18"/>
          </g>
        </svg>
        www.tklmsourcing.com
      </li>
      <li class="indent">000 Harbour View Street</li>
      <li class="indent">Area Name, NSW, 0000</li>
    </ul>
  </article>
</body>
</html>
```